Luxury Wine Label for New Startup Winery

We need a wine label for our new winery startup. We have worked with a local designer but do not feel the resulting label / logo have the elevation required to present our brand as a luxury wine. Our winery is called "Halvorsen Cellars" and we are focused on extremely high quality hand crafted artisan and estate wines from the Pacific Northwest.
We would like to see designs that utilize a tree line, or other imagery that represents the "Halvorsen" part of our company name. Another interesting feature could be wood grain.
A logo will be required based on your design so please design with this in mind:
This logo should be consistent with the wine bottle label design, and should be representative of our high end exclusive wine while giving a sense of place (Oregon/ Pacific Northwest.)
I will supply an image of the design we received from our local designer, PLEASE NOTE: in general we do like wood grain and tree line concepts but feel the execution was poorly done.
ATTN: Logo design should be suitable for use on: Bottles (Red wine/rose/white wine), Bussiness cards, vehicle signage, business signage, etc
P.S.:
If you have a design that is not outside the box we are still interested in seeing it.
Label is for a burgundy style bottle with a label height of 3.5 - 4" and a width of 3.5-4"
any label <= 4"x4" and >=3.5"x3.5" will be acceptable:
HOWEVER Width should be greater than or equal to height due to the bottle format
Target Market(s)
Wine enthusiasts with adequate discretionary budgets to afford $100 bottles of wine.
Industry/Entity Type
Wine / Winery
Requirements
Must have
- A sense of luxury, a feel of exclusivity, and a theme consistent with our product and brand name
Nice to have
- Tree line, wood grain or other wood themes. Serif fonts
Should not have
- anything cheesy, off topic, hard to read script fonts or anything that makes the label hard to read from a few feet away or too busy

```html
<!DOCTYPE html>
<html lang="en">
<head>
<meta charset="utf-8">
<title>Halvorsen Cellars — Syrah Label</title>
<link href="https://fonts.googleapis.com/css2?family=Cinzel:wght@700&family=Oswald:wght@300;400&display=swap" rel="stylesheet">
<style>
  :root {
    --page: #ffffff;
    --label-cream: #e8e5df;
    --wine: #4a1218;
    --wine-mid: #6b2a30;
    --ember: #e0773a;
  }
  html, body {
    margin: 0;
    width: 1200px;
    height: 1200px;
    overflow: hidden;
    background: var(--page);
  }
  .label {
    position: absolute;
    left: 100px;
    top: 240px;
    width: 1000px;
    height: 722px;
    background: var(--label-cream);
    border-radius: 14px;
    overflow: hidden;
  }
  .brand {
    position: absolute;
    top: 60px;
    left: 0;
    right: 0;
    text-align: center;
  }
  .brand-square {
    display: block;
    width: 74px;
    height: 74px;
    margin: 0 auto 12px;
    background: var(--wine);
  }
  .brand-name {
    margin: 0;
    font-family: "Cinzel", serif;
    font-weight: 700;
    font-size: 34px;
    line-height: 33px;
    letter-spacing: 5px;
    color: var(--wine);
  }
  .region {
    margin: 8px 0 0;
    font-family: "Oswald", sans-serif;
    font-weight: 300;
    font-size: 20px;
    letter-spacing: 1px;
    color: var(--ember);
  }
  .varietal {
    position: absolute;
    top: 272px;
    left: 0;
    right: 0;
    margin: 0;
    text-align: center;
    font-family: "Cinzel", serif;
    font-weight: 700;
    font-size: 52px;
    line-height: 60px;
    letter-spacing: 6px;
    color: var(--wine);
    z-index: 1;
  }
  .treeline {
    position: absolute;
    left: 0;
    right: 0;
    top: 284px;
    height: 362px;
    background: linear-gradient(to bottom, var(--wine-mid), var(--wine) 75%);
    clip-path: polygon(0 4%, 12% 0, 30% 10%, 50% 26%, 70% 36%, 84% 48%, 91% 78%, 100% 76%, 100% 100%, 0 100%);
  }
  .details-band {
    position: absolute;
    left: 0;
    right: 0;
    bottom: 0;
    height: 78px;
    background: var(--wine);
    display: flex;
    align-items: center;
    justify-content: center;
    gap: 14px;
    font-family: "Oswald", sans-serif;
    font-weight: 400;
    color: var(--label-cream);
  }
  .details-small { font-size: 15px; }
  .details-year { font-size: 25px; font-weight: 300; }
  .details-sep { font-size: 15px; }
</style>
</head>
<body>
  <main class="label">
    <header class="brand">
      <span class="brand-square"></span>
      <h1 class="brand-name">Halvorsen<br>Cellars</h1>
      <p class="region">WILLAMETTE VALLEY, OREGON</p>
    </header>
    <h2 class="varietal">Syrah</h2>
    <div class="treeline" role="img" aria-label="Silhouetted forest tree line sloping down to the right, with birds in flight"></div>
    <footer class="details-band">
      <span class="details-small">750 ml</span>
      <span class="details-sep">/</span>
      <span class="details-year">2024</span>
      <span class="details-sep">/</span>
      <span class="details-small">13% Alc. Vol.</span>
    </footer>
  </main>
</body>
</html>
```